Emergency Vehicle Installer and Security Firm Needs a Business Card

Our company "Corvalt" need a business card for our Emergency Vehicle Equipment Installation and Infrastructure Security Business. We are contract designers, manufacturers and installers for Emergency Vehicle Fleets. This includes installation of Emergency Lights, Sirens, Vehicle Graphics and Radio Communications. We also supply this products to an international market. We also do consultant, and installation of high level security access, alarm and surveillance equipment for medium to large size businesses.

The design should represent a level of trust in our professionalism and expertise. It should visually display our ongoing relationship with the emergency services, but not overtake our commitment to high level security options.

Target Market(s)

Emergency Services and Businesses requiring high level security

Industry/Entity Type

Business

Contact Information for Business Card

*note complete details will be given to the winning designer for revising. The name "Mark Pell will be used to fill in name".

Mark Pell
Managing Director
Corvalt NZ Limited
Phone: +64 027 604 91352
Email: mark.pell@corvalt-example.co.nz

Requirements
Must have
• Card must be in black. Using our logo on the top as supplied. Designers should try having the reverse side as a blurred image of police lights (red and blue) with our logo in greyscale in the centre (this is not particularly a requirement, but feel free to play around with this option).
Nice to have
• A card design that looks good when spot UV printed. A clean compact and graphic design. A grey scale feel on the front (excluding logo, but you can play around with that idea). Rounded smooth text.
Should not have
• Will update this section as designs come through - feel free to submit what you feel would look good.

```html
<!DOCTYPE html>
<html lang="en">
<head>
<meta charset="utf-8">
<title>Corvalt Business Card</title>
<link href="https://fonts.googleapis.com/css2?family=Open+Sans:wght@400;600;700&family=Montserrat:wght@800&display=swap" rel="stylesheet">
<style>
  :root {
    --backdrop: #d9d6d2;
    --card-face: #eef0f1;
    --ink: #2a2a2a;
    --ink-soft: #3c3c3c;
    --accent-red: #c8141c;
    --panel-black: #141414;
    --highlight: #ffffff;
  }
  html, body {
    margin: 0;
    width: 1200px;
    height: 970px;
    overflow: hidden;
    background: var(--backdrop);
  }
  .canvas {
    position: relative;
    width: 1200px;
    height: 970px;
  }
  .business-card {
    position: absolute;
    left: 150px;
    top: 247px;
    width: 900px;
    height: 476px;
    background: var(--card-face);
    overflow: hidden;
    box-shadow: 0 10px 30px rgba(0,0,0,0.18);
  }
  .card-swoosh {
    position: absolute;
    inset: 0;
    width: 100%;
    height: 100%;
  }
  .brand-name {
    position: absolute;
    left: 0;
    width: 900px;
    top: 88px;
    text-align: center;
    font-family: "Montserrat", sans-serif;
    font-weight: 800;
    font-size: 64px;
    letter-spacing: 1px;
    color: var(--ink);
    margin: 0;
    padding-right: 60px;
    box-sizing: border-box;
  }
  .contact-block {
    position: absolute;
    left: 62px;
    top: 250px;
    font-family: "Open Sans", sans-serif;
    color: var(--ink-soft);
  }
  .contact-name {
    font-weight: 700;
    font-size: 22px;
    color: var(--ink);
    margin: 0;
    line-height: 1.2;
  }
  .contact-role {
    font-size: 21px;
    margin: 0 0 20px;
    line-height: 1.3;
  }
  .contact-company {
    font-size: 20px;
    color: var(--accent-red);
    margin: 0 0 18px;
  }
  .contact-line {
    display: flex;
    align-items: center;
    gap: 12px;
    font-size: 19px;
    margin: 0 0 10px;
  }
  .contact-line svg { width: 16px; height: 16px; flex: none; }
</style>
</head>
<body>
<main class="canvas">
  <section class="business-card" aria-label="Business card front">
    <svg class="card-swoosh" viewBox="0 0 900 476" preserveAspectRatio="none" aria-hidden="true">
      <path d="M735 0 C870 80 760 360 460 476 L900 476 L900 0 Z" fill="var(--panel-black)"/>
      <path d="M718 0 C850 80 745 360 440 476 L470 476 C760 360 868 80 735 0 Z" fill="var(--highlight)"/>
      <path d="M770 40 C820 170 700 370 420 476 L445 476 C730 370 830 170 778 40 Z" fill="var(--accent-red)"/>
    </svg>
    <h1 class="brand-name">CORVALT</h1>
    <div class="contact-block">
      <p class="contact-name">Mark Pell</p>
      <p class="contact-role">Managing Director</p>
      <p class="contact-company">Corvalt NZ Limited</p>
      <p class="contact-line">
        <svg viewBox="0 0 24 24"><path fill="#333" d="M6.6 10.8a15 15 0 0 0 6.6 6.6l2.2-2.2c.3-.3.7-.4 1-.2 1.1.4 2.3.6 3.6.6.6 0 1 .4 1 1V20c0 .6-.4 1-1 1A17 17 0 0 1 3 4c0-.6.4-1 1-1h3.5c.6 0 1 .4 1 1 0 1.3.2 2.5.6 3.6.1.3 0 .7-.2 1z"/></svg>
        +64 027 604 91352
      </p>
      <p class="contact-line">
        <svg viewBox="0 0 24 24"><text x="12" y="18" text-anchor="middle" font-family="Open Sans, sans-serif" font-weight="700" font-size="20" fill="#333">@</text></svg>
        mark.pell@corvalt-example.co.nz
      </p>
    </div>
  </section>
</main>
</body>
</html>
```